Keelrock Data Partners (KDP) Business Card Design

I would like to create double-sided business cards that contain:
1) Name: Marcus Tolliver
2) Phone Number: +1 (555) 018-2947
3) Email: Marcus.Tolliver@KeelrockDataPartners.com
4) Website: KeelrockDataPartners.com

I would like to include my logo and a color scheme similar to the Vantorra Grand Prix Kelvex team color scheme (black, silver, greenish-blue – but can also include regular blue)

Logos attached.

What we do: Our company develops and delivers innovative and pragmatic information technology and cybersecurity risk and compliance solutions for organizations in the commercial market as well as the federal, and state/local sectors.

```html
<!DOCTYPE html>
<html lang="en">
<head>
<meta charset="utf-8">
<title>Keelrock Data Partners — Business Card</title>
<link rel="stylesheet" href="https://fonts.googleapis.com/css2?family=Roboto:wght@300;400;500&display=swap">
<style>
  :root {
    --backdrop: #ececec;
    --card-black: #0f1012;
    --card-charcoal: #393a3c;
    --wave-grey-top: #1c1d1f;
    --wave-grey-low: #5c5e61;
    --teal: #22bcc4;
    --teal-light: #bfe9ec;
    --silver: #c9ccce;
    --white: #f1f2f3;
  }
  * { margin: 0; padding: 0; box-sizing: border-box; }
  html, body {
    width: 1200px;
    height: 900px;
    overflow: hidden;
    background: var(--backdrop);
    font-family: "Roboto", Arial, sans-serif;
  }
  .canvas {
    position: relative;
    width: 1200px;
    height: 900px;
  }
  .card {
    position: absolute;
    left: 355px;
    width: 491px;
    height: 280px;
    overflow: hidden;
  }
  .card-front {
    top: 120px;
    background: linear-gradient(90deg, var(--card-charcoal) 0%, #222325 50%, var(--card-black) 100%);
    display: flex;
    align-items: center;
    justify-content: center;
  }
  .front-name {
    color: var(--silver);
    font-weight: 400;
    font-size: 24px;
    letter-spacing: 1px;
  }
  .card-back {
    top: 482px;
    background: var(--card-black);
  }
  .wave {
    position: absolute;
    inset: 0;
    width: 491px;
    height: 280px;
  }
  .back-company {
    position: absolute;
    left: 30px;
    top: 30px;
    color: var(--silver);
    font-weight: 400;
    font-size: 15px;
    line-height: 17px;
    letter-spacing: 1.5px;
    text-transform: uppercase;
  }
  .holder {
    position: absolute;
    left: 268px;
    top: 110px;
    width: 180px;
    text-align: center;
  }
  .holder-name {
    color: var(--white);
    font-size: 18px;
    font-weight: 400;
  }
  .holder-title {
    margin-top: 4px;
    color: var(--teal);
    font-size: 13px;
    font-weight: 400;
  }
  .contact {
    position: absolute;
    left: 17px;
    top: 199px;
    list-style: none;
    color: var(--white);
    font-size: 14px;
    line-height: 18.5px;
    font-weight: 400;
  }
  .contact-label {
    display: inline-block;
    width: 24px;
  }
</style>
</head>
<body>
<main class="canvas">
  <section class="card card-front" aria-label="Card front">
    <p class="front-name">Keelrock Data Partners</p>
  </section>

  <section class="card card-back" aria-label="Card back">
    <svg class="wave" viewBox="0 0 419 239" preserveAspectRatio="none" aria-hidden="true">
      <defs>
        <linearGradient id="upper-fade" x1="0" y1="0" x2="0" y2="1">
          <stop offset="0" stop-color="var(--wave-grey-top)"/>
          <stop offset="1" stop-color="var(--wave-grey-low)"/>
        </linearGradient>
      </defs>
      <path fill="var(--teal-light)" d="M0,0 H419 V94 C400,84 370,76 330,76 C280,80 240,104 180,128 C120,150 60,160 0,150 Z"/>
      <path fill="var(--teal)" d="M0,0 H419 V91 C400,80 370,70 330,70 C270,72 230,98 170,120 C110,140 50,140 0,128 Z"/>
      <path fill="url(#upper-fade)" d="M0,0 H419 V88 C395,72 365,58 330,57 C250,55 200,105 140,117 C90,127 40,118 0,90 Z"/>
    </svg>

    <p class="back-company">Keelrock<br>Data<br>Partners</p>

    <div class="holder">
      <p class="holder-name">Marcus Tolliver</p>
      <p class="holder-title">Chief Executive Officer</p>
    </div>

    <ul class="contact">
      <li><span class="contact-label">P:</span>+1 (555) 018-2947</li>
      <li><span class="contact-label">@:</span>Marcus.Tolliver@KeelrockDataPartners.com</li>
      <li><span class="contact-label">W:</span>KeelrockDataPartners.com</li>
    </ul>
  </section>
</main>
</body>
</html>
```